Unique and original Business Card for Financial Services Business

I have moved premises and need to change the detail on my business card so thought now is a good time for a re-design. Looking for something professional and modern with colours to fit in with out logo. Like the idea of foil or embossing if that works but not a must have but I do want something that stands out and that I could not design myself.

Once business card is designed I will also be looking to get letterhead and flyers done but want the business card concept in place first.

The majority of designs I am receiving are generic and template based. I am looking for something unique and original. We have some great design elements in our logo, think outside the box and show me something that stands out from the crowd.

Target Market(s)

Business Professionals

Industry/Entity Type

Finance

Contact Information for Business Card

Name: Delia Norwood Phone 0473 958 162 Address PO Box 8617 Mossvale NSW 2389 Email info@steadyharbourfinancialservices.com.au website www.steadyharbourfinancialservices.com.au

Font styles to use
Other font styles liked:
• Ralway

Requirements
Should not have
• No black backgrounds please

```html
<!DOCTYPE html>
<html lang="en">
<head>
<meta charset="utf-8">
<title>Steady Harbour Financial Services – Business Card</title>
<link href="https://fonts.googleapis.com/css2?family=Montserrat:wght@400;600;700&family=Raleway:wght@300&display=swap" rel="stylesheet">
<style>
  :root {
    --teal: #1a9e9a;
    --teal-deep: #0f8a88;
    --ink: #222428;
    --card: #ffffff;
    --card-shade: #f3f3f3;
    --backdrop: #e4e5e7;
    --steel-dark: #5c5c5e;
    --steel-light: #f2f2f2;
  }
  * { box-sizing: border-box; margin: 0; padding: 0; }
  html, body {
    width: 1200px; height: 1200px; overflow: hidden;
    background: var(--backdrop);
  }
  .sheet {
    position: relative; width: 1200px; height: 1200px;
  }
  .card {
    position: absolute; left: 170px;
    width: 860px; height: 490px;
    border-radius: 42px;
    background: linear-gradient(180deg, var(--card) 70%, var(--card-shade) 100%);
    box-shadow: 0 14px 30px rgba(0,0,0,0.18);
    overflow: hidden;
  }
  .card--front { top: 90px; }
  .card--back { top: 620px; }

  /* contact side */
  .contact {
    position: absolute; left: 70px; top: 150px;
    font-family: "Montserrat", sans-serif; color: var(--ink);
  }
  .contact__name {
    font-weight: 700; font-size: 38px; letter-spacing: 1px;
    color: var(--teal); text-transform: uppercase;
    margin-bottom: 14px;
  }
  .contact__list { list-style: none; }
  .contact__item {
    display: flex; align-items: center; gap: 14px;
    font-size: 17px; line-height: 30px;
  }
  .contact__item--phone { font-size: 22px; line-height: 34px; }
  .contact__icon { width: 22px; height: 22px; flex: none; fill: var(--teal); }

  /* brand lockup */
  .brand {
    position: absolute; display: flex; align-items: center;
    font-family: "Raleway", sans-serif; font-weight: 300;
    color: var(--teal-deep);
  }
  .brand__mark { flex: none; background: var(--teal); }
  .brand__text { display: flex; flex-direction: column; line-height: 1.05; }
  .brand--small { right: 60px; top: 120px; gap: 16px; }
  .brand--small .brand__mark { width: 54px; height: 54px; }
  .brand--small .brand__name { font-size: 32px; }
  .brand--small .brand__tag { font-size: 16px; letter-spacing: 5px; }
  .brand--large { left: 200px; top: 150px; gap: 28px; }
  .brand--large .brand__mark { width: 96px; height: 96px; }
  .brand--large .brand__name { font-size: 54px; }
  .brand--large .brand__tag { font-size: 25px; letter-spacing: 9px; }

  /* bands */
  .band { position: absolute; bottom: 0; }
  .band--teal {
    left: 0; width: 530px; height: 22px;
    background: linear-gradient(90deg, var(--teal-deep), var(--teal));
  }
  .band--steel {
    right: 0; height: 36px;
    background: linear-gradient(90deg, var(--steel-dark) 0%, #a9a9ab 30%, var(--steel-light) 55%, #9c9c9e 80%, var(--steel-dark) 100%);
  }
  .card--front .band--steel { left: 542px; }
  .card--back .band--steel { left: 380px; height: 46px; }
</style>
</head>
<body>
<main class="sheet">

  <section class="card card--front" aria-label="Business card front">
    <div class="contact">
      <h1 class="contact__name">Delia Norwood</h1>
      <ul class="contact__list">
        <li class="contact__item contact__item--phone">
          <svg class="contact__icon" viewBox="0 0 24 24"><path d="M6.6 10.8c1.4 2.8 3.8 5.1 6.6 6.6l2.2-2.2c.3-.3.7-.4 1-.2 1.1.4 2.3.6 3.6.6.6 0 1 .4 1 1V20c0 .6-.4 1-1 1C10.6 21 3 13.4 3 4c0-.6.4-1 1-1h3.5c.6 0 1 .4 1 1 0 1.3.2 2.5.6 3.6.1.3 0 .7-.2 1z"/></svg>
          0473 958 162
        </li>
        <li class="contact__item">
          <svg class="contact__icon" viewBox="0 0 24 24"><path d="M12 2a10 10 0 1 0 0 20 10 10 0 0 0 0-20zm6.9 6h-3a15 15 0 0 0-1.3-3.9A8 8 0 0 1 18.9 8zM12 4c.8 1.2 1.5 2.5 1.9 4h-3.8c.4-1.5 1.1-2.8 1.9-4zM4.3 14a8 8 0 0 1 0-4h3.4a16 16 0 0 0 0 4zm.8 2h3a15 15 0 0 0 1.3 3.9A8 8 0 0 1 5.1 16zm3-8h-3a8 8 0 0 1 4.3-3.9C8.8 5.2 8.4 6.6 8.1 8zM12 20c-.8-1.2-1.5-2.5-1.9-4h3.8c-.4 1.5-1.1 2.8-1.9 4zm2.3-6H9.7a14 14 0 0 1 0-4h4.6a14 14 0 0 1 0 4zm.3 5.9c.6-1.2 1-2.5 1.3-3.9h3a8 8 0 0 1-4.3 3.9zm1.7-5.9a16 16 0 0 0 0-4h3.4a8 8 0 0 1 0 4z"/></svg>
          www.steadyharbourfinancialservices.com.au
        </li>
        <li class="contact__item">
          <svg class="contact__icon" viewBox="0 0 24 24"><path d="M2 5h20v14H2zm2 2v.4l8 5.2 8-5.2V7zm0 2.8V17h16V9.8l-8 5.2z"/></svg>
          info@steadyharbourfinancialservices.com.au
        </li>
        <li class="contact__item">
          <svg class="contact__icon" viewBox="0 0 24 24"><path d="M12 2a7 7 0 0 0-7 7c0 5.2 7 13 7 13s7-7.8 7-13a7 7 0 0 0-7-7zm0 9.5a2.5 2.5 0 1 1 0-5 2.5 2.5 0 0 1 0 5z"/></svg>
          PO Box 8617 Mossvale NSW 2389
        </li>
      </ul>
    </div>

    <div class="brand brand--small">
      <span class="brand__mark"></span>
      <span class="brand__text">
        <span class="brand__name">STEADY HARBOUR</span>
        <span class="brand__tag">Financial Services</span>
      </span>
    </div>

    <div class="band band--teal"></div>
    <div class="band band--steel"></div>
  </section>

  <section class="card card--back" aria-label="Business card back">
    <div class="brand brand--large">
      <span class="brand__mark"></span>
      <span class="brand__text">
        <span class="brand__name">STEADY HARBOUR</span>
        <span class="brand__tag">Financial Services</span>
      </span>
    </div>
    <div class="band band--steel"></div>
  </section>

</main>
</body>
</html>
```